【概要】明治創業の老舗買取店の公式サイトのリニューアルに伴い、サイトに掲載するデザインを大募集します! 1からデザインを考えて頂く訳ではなく、ベースのデザインをもとに文章は変えずに、 老舗感を残しつつ、高級感のあるデザインにリニューアルして頂きたいと考えています。 【依頼内容】 ・サイズ: PC版ヘッダー①:横幅1050px、縦幅400px PC版ヘッダー②:横幅1450px、縦幅1050px SP版ヘッダー:横幅750px、縦幅1050px ★まずは①のデザインでご提案下さい。採用が確定しましたら、デザインはそのままに微調整いただき、上記の3サイズを納品頂きたいです。★ ・ 種類:3種類(店舗情報と金について2種類) ※詳細別紙参照。(ソラノ転送便にて) ⇒https://35.soranoten.jp/0611-k52793a18e2584f8d7a30ecb793773017 ・素材の用意(画像や動画): 素材や詳細資料は上記ソラノ転送便にて送らせて頂きます。 但し、あまり素材がないのでこちらで用意する素材以外にも使用していただいて構いません。デザイン優先でお勧めがあれば提案頂きたいです。 細かな希望は別紙資料に記載してありますのでそちらをご確認下さい。サイトを見て来店が増えるようなデザインにしたいです。 【デザインイメージ】 ※詳細は別紙参照 ・ターゲット層:30代~80代 ・雰囲気:老舗の雰囲気を残しつつ、高級感のあるデザインにしたいです。 ・ベースカラー: 店舗情報⇒ロゴカラーと同じ赤と青 金2種類⇒ゴールド 【納品フォーマット】 ・Illustrator形式(アウトラインデータ/編集データ)→後に編集する可能性があるためとなります。 ・PDFデータ ・PNGデータ(確認用) ・フォントファイル ※尚、採用したデザインの権利に関しては全て依頼者に寄与するものとします。 気に入るデザインがみつかり採用と納品が確定しましたら、追加で複数、サイトに掲載するデザインを 依頼させて頂く予定です。デザインの数と費用は別途相談させて頂きます。 今回以降も継続してお仕事のできる方、大歓迎です。 【 契約金額(税抜) 】 ・4万円 ※契約金額(税込)からシステム利用料を差し引いた金額が、ワーカーさまの受取金額となります。 その他ご質問等ありましたら、気軽にお問い合わせください。ご応募をお待ちしております! |
どの提案も素敵でした!沢山のご応募ありがとうございました!特にデザインがイメージと近く、対応も迅速でしたため採用させていただきました!
ご応募いただきありがとうございました!

```html
<!DOCTYPE html>
<html lang="ja">
<head>
<meta charset="utf-8">
<title>買取店 サイトヘッダー</title>
<link rel="stylesheet" href="https://fonts.googleapis.com/css2?family=Noto+Sans+JP:wght@400;500;700;900&family=Montserrat:ital,wght@0,300;0,700;1,300&display=swap">
<style>
:root{
  --canvas:#4a4a4c;
  --navy:#14207a;
  --navy-deep:#0b1250;
  --blue:#2a3aa8;
  --white:#ffffff;
  --ink:#1d2a88;
  --silver-1:#f4f5f8;
  --silver-2:#d9dce4;
  --gold-1:#f3d98a;
  --gold-2:#b8862c;
}
*{box-sizing:border-box;margin:0;padding:0}
html,body{width:1032px;height:1200px;overflow:hidden}
body{background:var(--canvas);font-family:"Noto Sans JP",sans-serif;position:relative}
.banner{position:absolute;left:27px;width:978px;overflow:hidden}
.abs{position:absolute}

/* store banner */
.store{top:27px;height:333px;background:var(--white)}
.store-lead{left:0;width:426px;height:333px;background:linear-gradient(135deg,#ffffff 0%,#eef1f8 100%)}
.lead-copy{left:0;top:24px;width:426px;text-align:center;color:var(--ink);font-weight:900;line-height:1.1}
.lead-copy .big{font-size:50px;letter-spacing:2px}
.lead-copy .mid{font-size:30px;margin:6px 0}
.goods-photo{left:40px;top:200px;width:210px;height:110px;border-radius:6px;background:linear-gradient(120deg,#f2eee4,#d8c89a 55%,#c9ccd6)}
.hours{left:250px;top:238px;width:170px;text-align:center;color:var(--ink);font-weight:700;font-size:21px;line-height:1.35}
.store-info{left:426px;width:552px;height:333px;background:linear-gradient(160deg,var(--blue) 0%,var(--navy-deep) 100%)}
.shop-photo{top:30px;height:180px;border-radius:2px}
.shop-a{left:28px;width:220px;background:linear-gradient(180deg,#e7ddc6,#b69e6d)}
.shop-b{left:280px;width:240px;background:linear-gradient(180deg,#cfd6dc,#8f867a)}
.shop-name{top:222px;color:var(--white);font-weight:700;font-size:25px;text-align:center}
.station{color:var(--white);font-size:13.5px;border:1.5px solid rgba(255,255,255,.85);border-radius:4px;text-align:center;line-height:1.35;padding:2px 4px}
.access{color:var(--white);font-weight:700;font-size:22px;text-align:center}

/* refining banner */
.refine{top:400px;height:347px;background:linear-gradient(90deg,var(--navy-deep) 0%,var(--navy) 55%,var(--blue) 100%)}
.tag{left:45px;top:22px;width:140px;height:32px;border:1.5px solid rgba(255,255,255,.8);border-radius:16px;color:var(--white);font-size:15px;text-align:center;line-height:29px;letter-spacing:2px}
.refine-title{left:45px;top:88px;color:var(--white);font-weight:700;font-size:58px;letter-spacing:6px}
.bubble{top:200px;width:112px;height:112px;border:1.5px solid rgba(255,255,255,.85);border-radius:50%;color:var(--white);font-size:12.5px;line-height:1.5;display:flex;align-items:center;justify-content:center;text-align:center}
.step-img{top:55px;width:112px;height:112px}
.ingot{background:linear-gradient(135deg,#f6e3a0,#c89a3a 60%,#8a6420)}
.melt{background:radial-gradient(circle at 50% 55%,#ffd36a,#e06a1a 45%,#3a1408 85%)}
.bars{background:linear-gradient(135deg,#f8e6a8,#d3a440 55%,#9c7427)}
.arrow{top:96px}
.step-cap{top:178px;width:130px;color:var(--white);font-size:15px;line-height:1.45;text-align:center}

/* precious banner */
.precious{top:795px;height:378px;background:radial-gradient(ellipse at 70% 40%,#ffffff 0%,var(--silver-1) 40%,var(--silver-2) 100%)}
.precious-label{left:72px;top:52px;font-family:"Montserrat",sans-serif;font-style:italic;font-weight:300;font-size:30px;color:var(--blue);letter-spacing:1px}
.precious-rule{left:72px;top:96px;width:230px;height:1.5px;background:var(--blue)}
.precious-title{left:60px;top:132px;width:520px;text-align:center;color:var(--ink);font-weight:700;font-size:68px;line-height:1.3;letter-spacing:4px}
.bar-gold{left:572px;top:38px;width:150px;height:320px;border-radius:10px;background:linear-gradient(120deg,var(--gold-1),var(--gold-2) 60%,#e7c46a)}
.bar-plat{left:712px;top:70px;width:130px;height:270px;border-radius:8px;background:linear-gradient(120deg,#f7f7f9,#b9bcc4 60%,#e4e6ea)}
.fee-badge{left:860px;top:172px;width:112px;height:112px;border-radius:50%;background:var(--white);box-shadow:0 2px 8px rgba(20,32,122,.15);text-align:center;color:var(--ink)}
.fee-badge .note{font-size:11.5px;font-weight:700;margin-top:16px}
.fee-badge .zero{font-family:"Montserrat",sans-serif;font-weight:700;font-size:58px;line-height:1;margin-top:2px}
.fee-badge .zero small{font-family:"Noto Sans JP",sans-serif;font-size:18px}
</style>
</head>
<body>

<section class="banner store">
  <div class="abs store-lead">
    <div class="abs lead-copy">
      <div class="big">買える</div>
      <div class="mid">ブランド品が</div>
      <div class="big">売れる</div>
    </div>
    <div class="abs goods-photo" role="img" aria-label="ブランドバッグと腕時計の写真"></div>
    <div class="abs hours">10:00 - 19:00<br>年中無休</div>
  </div>
  <div class="abs store-info">
    <div class="abs shop-photo shop-a" role="img" aria-label="港町地下店の店頭写真"></div>
    <div class="abs shop-photo shop-b" role="img" aria-label="本店の外観写真"></div>
    <div class="abs shop-name" style="left:28px;width:220px">港町地下店</div>
    <div class="abs station" style="left:38px;top:262px;width:200px">環状線港町駅　南改札口</div>
    <div class="abs station" style="left:38px;top:287px;width:200px;display:none"></div>
    <div class="abs shop-name" style="left:280px;width:240px">本店</div>
    <div class="abs station" style="left:292px;top:262px;width:216px">市営地下鉄<br>緑ヶ丘公園東駅</div>
    <div class="abs station" style="left:38px;top:290px;width:200px">東西線港町駅　中改札口</div>
    <div class="abs access" style="left:28px;top:300px;width:220px;display:none"></div>
    <div class="abs access" style="left:292px;top:300px;width:216px">徒歩 15分</div>
  </div>
</section>

<section class="banner refine">
  <div class="abs tag">おすすめ</div>
  <div class="abs refine-title">精錬分割加工</div>
  <div class="abs bubble" style="left:45px">資産を分割して<br>売却したい方</div>
  <div class="abs bubble" style="left:178px">金の節税対策<br>をお考えの方</div>
  <div class="abs bubble" style="left:311px">子や孫に分割<br>して金を渡して<br>おきたい方</div>

  <div class="abs step-img ingot" style="left:500px" role="img" aria-label="お客様の金インゴットの写真"></div>
  <svg class="abs arrow" style="left:618px" width="22" height="30" viewBox="0 0 22 30"><path d="M2 2 L20 15 L2 28 Z" fill="#ffffff"/></svg>
  <div class="abs step-img melt" style="left:648px" role="img" aria-label="精錬工場で金を溶かす写真"></div>
  <svg class="abs arrow" style="left:766px" width="22" height="30" viewBox="0 0 22 30"><path d="M2 2 L20 15 L2 28 Z" fill="#ffffff"/></svg>
  <div class="abs step-img bars" style="left:796px" role="img" aria-label="50gの金インゴットが並ぶ写真"></div>
  <div class="abs step-cap" style="left:491px">お客様の<br>インゴット</div>
  <div class="abs step-cap" style="left:639px">弊社提携工場で<br>精錬加工</div>
  <div class="abs step-cap" style="left:787px">50gの<br>インゴットに加工</div>
</section>

<section class="banner precious">
  <div class="abs precious-label">Precious</div>
  <div class="abs precious-rule"></div>
  <div class="abs precious-title">金・プラチナ<br>高価買取中</div>
  <div class="abs bar-plat" role="img" aria-label="プラチナインゴットの写真"></div>
  <div class="abs bar-gold" role="img" aria-label="金インゴットの写真"></div>
  <div class="abs fee-badge">
    <div class="note">査定料・手数料</div>
    <div class="zero">0<small>円</small></div>
  </div>
</section>

</body>
</html>
```